Pale Lantern Double Sided Flyer Design

We need a double sided flyer (1/3 of an A4 which is 99mm x 210mm) developed for our Newcastle(NSW) tour. This flyer will be placed in tourist information centres and hotels. We want it to direct people to our website or be able to make bookings over the phone.

About Us:-
We are a city walking tour company that runs tours day or night. We run both day and night and will incorporate real history / real Pale lantern. Some of the stories will be quite serious i.e.- there are infamous murders from 100 years ago, baffling court cases, even a bit of poetry written by murderers, suicides, love triangles, you name it. We will be telling the historical stories that tourists will not hear from any other tour provider. A bit of darkness, a bit of mystery and a bit of history theme.

We do no go for scares and let the very real stories deliver the entertainment for our guests. Our customers enjoy our tours, but it isn't light fun and frivolity. Our stories are being carefully crafted and are packed with unexpected twists, turns; revelations whilst remaining all 100% true. We deliver deep, rich, engaging stories.

Here are a few samples of quotes from the characters in our stories that may give you an idea of the kind of history we will cover:-

"There were bits of spines, bits of skulls, [and] finger bones spilled out all over the streets - I ended up filling three boxes. Children were playing with them for weeks”

"I had a close shave last night and now I want a close haircut.”

“She's a beautiful child', isn't she? She's the cause of all the trouble.”

“I did it because she would not come home with me.”

"I have killed my wife. I’m glad she’s dead.”

"Stand aside or I'll put a bullet through both of you."

“You villain, I'll teach you to take away my character."

“You’re not dead yet, you bastard!”

Our website, booking form and contact details can be viewed at www.palelantern.com.au

Target Market(s)

Tourists

Industry/Entity Type

Tour

Colors

Designer to choose colors to be used in the design.

Requirements
Must have
• Vertical orientation please.
• Please also include a reference to a discount offer of 25% using the promo code "WICK".
Nice to have
• FRONT FLYER INFORMATION
• - Pale Lantern Logo
• - "I have killed my wife; I'm glad she's dead."
• - Harbourside Hidden Lanes Walk
• - 25% Discount Offer Codeword WICK
• - web address at the base; www.palelantern.com.au
• BACK FLYER INFORMATION
• - "She's a beautiful child', isn't she? She's the cause of all the trouble.
• - Pale Lantern Logo at the base along with the web address www.palelantern.com.au
• - Blurb:- Pale lantern brings back Newcastle's hidden past, the forgotten past, the dark past that may not want to be remembered.
• Real stories from the streets around you. Discover the histories you won't hear anywhere else. The forgotten stories of yesteryear finally get a chance to be told. Through you they get to live again.
Should not have
• GENERAL
• Please do not include the phone number, email address or social media icons. We want to drive online bookings.

```html
<!DOCTYPE html>
<html lang="en">
<head>
<meta charset="utf-8">
<title>Pale Lantern – Flyer</title>
<link href="https://fonts.googleapis.com/css2?family=Montserrat:wght@500;600;700&family=Open+Sans:wght@700&family=PT+Serif:ital@1&display=swap" rel="stylesheet">
<style>
  :root{
    --backdrop:#e6e1d9;
    --paper:#efe3c6;
    --paper-edge:#d9c49a;
    --ink:#1d1b19;
    --red:#d0232b;
    --bar:#c8242b;
    --white:#ffffff;
    --photo-light:#8d8878;
    --photo-dark:#2f2c27;
  }
  *{margin:0;padding:0;box-sizing:border-box}
  html,body{width:1200px;height:998px;overflow:hidden;background:var(--backdrop)}
  .canvas{position:relative;width:1200px;height:998px}

  .flyer{
    position:absolute;top:49px;width:415px;height:878px;overflow:hidden;
    background:
      radial-gradient(ellipse 60% 30% at 5% 45%, rgba(208,35,43,.28), transparent 70%),
      radial-gradient(ellipse 50% 40% at 95% 20%, rgba(196,150,80,.35), transparent 70%),
      radial-gradient(ellipse 90% 70% at 50% 50%, var(--paper), var(--paper-edge));
    box-shadow:0 4px 10px rgba(0,0,0,.35);
    color:var(--ink);text-align:center;
  }
  .flyer--front{left:155px}
  .flyer--back{left:632px;
    background:
      radial-gradient(ellipse 30% 30% at 3% 18%, rgba(208,35,43,.35), transparent 70%),
      radial-gradient(ellipse 90% 70% at 50% 50%, var(--paper), var(--paper-edge));}

  .brand{position:absolute;left:0;right:0;font-family:"Montserrat",sans-serif;font-weight:600;color:var(--ink);letter-spacing:1px}
  .brand__mark{position:absolute;border:4px solid var(--ink);border-radius:50%}

  .front__mark{left:157px;top:40px;width:100px;height:100px}
  .front__name{top:158px;font-size:40px;line-height:48px}

  .quote{position:absolute;left:0;right:0;font-family:"PT Serif",serif;font-style:italic;font-size:22px;line-height:27px;color:var(--ink)}
  .front__quote{top:234px}
  .back__quote{top:42px;font-size:22px;line-height:28px}

  .tour-title{position:absolute;left:0;right:0;top:306px;font-family:"Montserrat",sans-serif;font-weight:700;font-size:23px;line-height:29px;text-transform:uppercase}
  .tour-title__accent{color:var(--red)}

  .offer{position:absolute;left:236px;top:400px;width:148px;height:148px}

  .photo{position:absolute;left:0;right:0}
  .front__photo{top:507px;height:331px;
    background:linear-gradient(180deg,rgba(239,227,198,0) 0%,var(--photo-light) 18%,#5c574c 55%,var(--photo-dark) 100%)}
  .back__photo{top:284px;height:212px;
    background:linear-gradient(160deg,#a9a595 0%,#77726a 40%,var(--photo-dark) 100%)}

  .blurb{position:absolute;left:50%;transform:translateX(-50%);font-family:"Open Sans",sans-serif;font-weight:700;font-size:16px;line-height:21.5px;color:var(--ink)}
  .back__intro{top:158px;width:270px}
  .back__body{top:542px;width:340px}

  .back__mark{left:166px;top:714px;width:30px;height:30px}
  .back__name{top:752px;font-size:22px;line-height:28px}
  .back__mark{left:192px;top:712px}

  .web-bar{position:absolute;left:0;right:0;bottom:0;height:40px;background:var(--bar);color:var(--white);
    font-family:"Montserrat",sans-serif;font-weight:700;font-size:18px;line-height:40px;letter-spacing:.5px;text-transform:uppercase}
</style>
</head>
<body>
<main class="canvas">

  <section class="flyer flyer--front">
    <span class="brand__mark front__mark"></span>
    <h1 class="brand front__name">PALE LANTERN</h1>
    <p class="quote front__quote">"I have killed my wife;<br>I'm glad she's dead."</p>
    <h2 class="tour-title">Harbourside<br><span class="tour-title__accent">Hidden Lanes</span><br>Walk</h2>

    <svg class="offer" viewBox="0 0 148 148" aria-label="25% discount offer, codeword WICK">
      <defs><path id="codeArc" d="M22,74 A52,52 0 0 0 126,74"/></defs>
      <circle cx="74" cy="74" r="73" fill="var(--ink)"/>
      <circle cx="74" cy="74" r="67" fill="none" stroke="var(--paper)" stroke-width="1.5"/>
      <text x="74" y="64" text-anchor="middle" font-family="Montserrat,sans-serif" font-weight="700" font-size="30" fill="#fff">25%</text>
      <text x="74" y="84" text-anchor="middle" font-family="Montserrat,sans-serif" font-weight="600" font-size="13" fill="#fff">DISCOUNT</text>
      <text x="74" y="99" text-anchor="middle" font-family="Montserrat,sans-serif" font-weight="600" font-size="13" fill="#fff">OFFER</text>
      <text font-family="Montserrat,sans-serif" font-weight="600" font-size="11" fill="#d8b878" letter-spacing="1">
        <textPath href="#codeArc" startOffset="50%" text-anchor="middle">CODEWORD: WICK</textPath>
      </text>
    </svg>

    <div class="photo front__photo" role="img" aria-label="Sepia photograph of a historic sandstone street with Victorian buildings"></div>
    <div class="web-bar">www.palelantern.com.au</div>
  </section>

  <section class="flyer flyer--back">
    <p class="quote back__quote">"She's a beautiful child', isn't she?<br>She's the cause of all the trouble.</p>
    <p class="blurb back__intro">Pale lantern brings back Newcastle's hidden past, the forgotten past, the dark past that may not want to be remembered.</p>
    <div class="photo back__photo" role="img" aria-label="Old sepia photograph of a tram on a misty city street"></div>
    <p class="blurb back__body">Real stories from the streets around you. Discover the histories you won't hear anywhere else. The forgotten stories of yesteryear finally get a chance to be told. Through you they get to live again.</p>
    <span class="brand__mark back__mark"></span>
    <p class="brand back__name">PALE LANTERN</p>
    <div class="web-bar">www.palelantern.com.au</div>
  </section>

</main>
</body>
</html>
```